Consulting company, design, Interior design in commercial real estate (Tertiai sector *

Company name: VORANDEL: from the Greek Evexia well-being, was born from a desire to combine well-being and work. By the choice of design, materials, design and furniture, everything is thought from this perspective

Logo: Essay with Möbius Ribbon and / or with the infinite acronym / and or triangle ...
Sentences to write:
"The exclusive partner for your development projects"
"Consulting - Design - Construction"
"We manage EVERYTHING for you"

On the back: Photo (attached; if photo is not clear, another photo can be provided) with company name and "VORANDEL, Excellence and reliability"
My name / First name: provided later (double name), Manager
Address: supplied later
Tel: supplied later
Website: www. vorandel.com
Colors: Black, gold and white. Other admissible colors
See attached files

Real estate business

Nom de l'entreprise : VORANDEL : du grec Evexia bien être, est né d'une volonté de faire rimer bien être et travail. Par le choix de la conception, des matériaux, du design et du mobilier, tout est pensé dans cette optique

Logo : Essai avec Ruban de Möbius et /ou avec le sigle infini / et ou triangle...
Phrases à inscrire :
"Le partenaire exclusif de vos projets d'aménagement"
"Conseil - Conception - Construction"
"Nous gérons TOUT pour vous"

Au verso : Photo (ci-jointe ; si photo pas nette, une autre photo peut être fournie) avec nom de l'entreprise et Mention "VORANDEL, Excellence et fiabilité"
Mon nom / Prénom : fourni ultérieurement (prénom double), Gérant
Adresse : fourni ultérieurement
Tél : fourni ultérieurement
Site Web : www. vorandel.com
Couleurs : Noir, doré et blanc. Autre couleurs recevables
Voir fichiers ci-joint

• My project must be simple, clear, neat and design.
The business card must catch the customer

```html
<!DOCTYPE html>
<html lang="en">
<head>
<meta charset="UTF-8">
<title>Vorandel Business Card</title>
<link href="https://fonts.googleapis.com/css2?family=Barlow+Condensed:wght@500;700&family=Montserrat:wght@400;500;600&display=swap" rel="stylesheet">
<style>
  :root {
    --backdrop: #1c1c1c;
    --card: #0e0e0e;
    --gold: #d9a520;
    --gold-soft: #b88a1c;
    --white: #ffffff;
    --grey: #d6d6d6;
  }
  * { box-sizing: border-box; margin: 0; padding: 0; }
  html, body { width: 1200px; height: 900px; overflow: hidden; }
  body {
    background: var(--backdrop);
    position: relative;
    font-family: "Montserrat", sans-serif;
    color: var(--white);
  }
  .card {
    position: absolute;
    width: 700px;
    height: 400px;
    background: var(--card);
    box-shadow: 0 12px 30px rgba(0,0,0,0.55);
  }
  .card-front { left: 140px; top: 40px; }
  .card-back { left: 360px; top: 470px; }

  .brand-name {
    font-family: "Montserrat", sans-serif;
    font-weight: 600;
    color: var(--white);
    letter-spacing: 2px;
    line-height: 1;
    text-align: center;
  }

  /* Front */
  .card-front .brand-name { position: absolute; top: 82px; left: 0; right: 0; font-size: 50px; }
  .front-copy {
    position: absolute;
    top: 200px; left: 0; right: 0;
    text-align: center;
    font-family: "Barlow Condensed", sans-serif;
    text-transform: uppercase;
  }
  .partner-line { font-size: 18px; font-weight: 500; letter-spacing: 0.6px; }
  .services-line { font-size: 34px; font-weight: 700; letter-spacing: 0.5px; margin-top: 2px; }
  .promise-line { font-size: 16px; font-weight: 500; letter-spacing: 0.6px; margin-top: 18px; }
  .front-rule {
    position: absolute;
    left: 225px; width: 250px; top: 352px;
    height: 2px;
    background: var(--gold);
  }

  /* Back */
  .card-back .brand-name { position: absolute; top: 152px; left: 40px; width: 300px; font-size: 42px; }
  .person { position: absolute; left: 410px; top: 70px; }
  .person-name { font-size: 28px; font-weight: 500; letter-spacing: 1px; text-transform: uppercase; }
  .person-title { font-size: 14px; color: var(--grey); margin-top: 2px; }
  .contact-list { position: absolute; left: 410px; top: 145px; list-style: none; }
  .contact-list li {
    display: flex; align-items: center; gap: 10px;
    font-size: 15px; line-height: 24px; color: var(--white);
  }
  .contact-list svg { width: 14px; height: 14px; fill: var(--gold); flex: none; }
  .back-rule {
    position: absolute;
    left: 410px; right: 40px; top: 232px;
    height: 1px; background: var(--gold-soft);
  }
  .address {
    position: absolute; left: 410px; top: 250px;
    font-size: 15px; line-height: 22px; color: var(--white);
    font-style: normal;
  }
  .base-rule {
    position: absolute;
    left: 40px; width: 300px; bottom: 40px;
    height: 1px; background: var(--gold-soft);
  }
</style>
</head>
<body>

  <section class="card card-front">
    <div class="brand-name">VORANDEL</div>
    <div class="front-copy">
      <p class="partner-line">The exclusive partner for your development projects</p>
      <p class="services-line">Consulting - Design - Construction</p>
      <p class="promise-line">We manage everything for you</p>
    </div>
    <div class="front-rule"></div>
  </section>

  <section class="card card-back">
    <div class="brand-name">VORANDEL</div>

    <div class="person">
      <p class="person-name">Marc Delorme</p>
      <p class="person-title">Executive Director</p>
    </div>

    <ul class="contact-list">
      <li>
        <svg viewBox="0 0 24 24" aria-hidden="true"><path d="M6.6 10.8a15.1 15.1 0 0 0 6.6 6.6l2.2-2.2c.3-.3.7-.4 1-.2 1.1.4 2.3.6 3.6.6.6 0 1 .4 1 1V20c0 .6-.4 1-1 1A17 17 0 0 1 3 4c0-.6.4-1 1-1h3.5c.6 0 1 .4 1 1 0 1.3.2 2.5.6 3.6.1.3 0 .7-.2 1z"/></svg>
        000-000-0000
      </li>
      <li>
        <svg viewBox="0 0 24 24" aria-hidden="true"><path d="M2 5h20v14H2zM4 7v.5l8 5 8-5V7l-8 5z"/></svg>
        marc@vorandel.com
      </li>
      <li>
        <svg viewBox="0 0 24 24" aria-hidden="true"><path d="M12 2a10 10 0 1 0 0 20 10 10 0 0 0 0-20zm6.9 6h-3a15.6 15.6 0 0 0-1.3-3.9A8 8 0 0 1 18.9 8zM12 4c.8 1.2 1.5 2.5 1.9 4h-3.8c.4-1.5 1.1-2.8 1.9-4zM4.3 14a8 8 0 0 1 0-4h3.4a16 16 0 0 0 0 4zm.8 2h3a15.6 15.6 0 0 0 1.3 3.9A8 8 0 0 1 5.1 16zm3-8h-3a8 8 0 0 1 4.3-3.9A15.6 15.6 0 0 0 8.1 8zM12 20c-.8-1.2-1.5-2.5-1.9-4h3.8c-.4 1.5-1.1 2.8-1.9 4zm2.3-6H9.7a14.7 14.7 0 0 1 0-4h4.6a14.7 14.7 0 0 1 0 4zm.3 5.9c.6-1.2 1-2.5 1.3-3.9h3a8 8 0 0 1-4.3 3.9zm1.7-5.9a16 16 0 0 0 0-4h3.4a8 8 0 0 1 0 4z"/></svg>
        www.vorandel.com
      </li>
    </ul>

    <div class="back-rule"></div>

    <address class="address">
      00000 Harlow Street, Suite 000<br>
      Brenford Hill, ON, L0C 000
    </address>

    <div class="base-rule"></div>
  </section>

</body>
</html>
```